Modern Business Card For A Digital Advertising Company

I'll be print on the Tally Prints Velvet paper http://us.tallyprints-example.com/products/velvet/business-cards.html
Need's to be modern and use the color palette of the logo or gray scales. I think integrating the pixelation of the logo in to the card and having it wrap from one side to the other could be interesting. My company provides ad operations, web development, and number of other services to websites around the world. You can see my website at http://www.brightorbitads-example.com
Contact info on the card needs to have
Dana Welby
President
p.555.308.4127
dana@brightorbitads-example.com
http://www.brightorbitads-example.com
Doesn't necessarily need to be in that order
Target Market(s)
Website owners
Industry/Entity Type
Business
Look and feel
Each slider illustrates characteristics of the customer's brand and the style your logo design should communicate.

```html
<!DOCTYPE html>
<html lang="en">
<head>
<meta charset="utf-8">
<title>Bright Orbit Ads – Business Card</title>
<link href="https://fonts.googleapis.com/css2?family=Open+Sans:wght@300;400;600;700&display=swap" rel="stylesheet">
<style>
  :root {
    --page-bg: #ececec;
    --card-white: #ffffff;
    --brand-green: #85c226;
    --brand-green-light: #b3da72;
    --ink: #231f20;
    --ink-soft: #333333;
    --white: #ffffff;
  }
  * { box-sizing: border-box; margin: 0; padding: 0; }
  html, body { width: 1200px; height: 1000px; overflow: hidden; }
  body {
    background: var(--page-bg);
    font-family: "Open Sans", Arial, sans-serif;
    position: relative;
  }
  .card {
    position: absolute;
    left: 300px;
    width: 600px;
    height: 370px;
    overflow: hidden;
    box-shadow: 0 3px 10px rgba(0,0,0,0.12);
  }
  .card--front { top: 90px; background: var(--card-white); }
  .card--back  { top: 540px; background: var(--brand-green); }

  .front__frame { position: absolute; inset: 0; }

  .front__name {
    position: absolute; left: 28px; top: 52px;
    font-size: 27px; font-weight: 700; color: var(--ink);
    letter-spacing: 0.2px;
  }
  .front__title {
    position: absolute; left: 28px; top: 97px;
    font-size: 17px; font-weight: 400; color: var(--ink);
  }
  .contact {
    position: absolute; left: 28px; top: 262px;
    list-style: none;
  }
  .contact__item {
    display: flex; align-items: center;
    height: 27px;
    font-size: 13.5px; color: var(--ink-soft);
    white-space: nowrap;
  }
  .contact__icon {
    width: 16px; height: 16px; border-radius: 50%;
    background: var(--brand-green); color: var(--white);
    font-size: 11px; line-height: 15px; text-align: center;
    margin-right: 12px; flex: none;
  }
  .front__pixels {
    position: absolute; left: 302px; top: 302px;
    width: 88px; height: 42px;
    background: linear-gradient(90deg, var(--brand-green-light), var(--brand-green));
  }
  .brand {
    position: absolute; left: 428px; top: 190px;
    width: 150px;
    display: flex; flex-direction: column; align-items: flex-start;
  }
  .brand__mark {
    width: 44px; height: 44px; background: var(--brand-green);
    margin-bottom: 14px;
  }
  .brand__name {
    font-size: 24px; font-weight: 700; line-height: 1.05;
    color: var(--brand-green);
  }

  .back__url {
    position: absolute; left: 0; right: 0; top: 140px;
    text-align: center; color: var(--white);
    white-space: nowrap;
  }
  .back__url-prefix, .back__url-suffix {
    font-size: 17px; font-weight: 300; opacity: 0.6;
  }
  .back__url-domain { font-size: 30px; font-weight: 600; }
  .back__pixels {
    position: absolute; left: 385px; top: 265px;
    width: 185px; height: 70px;
    background: linear-gradient(90deg, rgba(255,255,255,0.15), rgba(255,255,255,0.35));
  }
</style>
</head>
<body>
  <section class="card card--front">
    <svg class="front__frame" width="600" height="370" viewBox="0 0 600 370" aria-hidden="true">
      <path d="M28 90 H270 A125 125 0 0 1 395 215 V345" fill="none" stroke="var(--brand-green)" stroke-width="4"/>
    </svg>
    <h1 class="front__name">Dana Welby</h1>
    <p class="front__title">President</p>
    <ul class="contact">
      <li class="contact__item"><span class="contact__icon">p</span>555.308.4127</li>
      <li class="contact__item"><span class="contact__icon">e</span>dana@brightorbitads-example.com</li>
      <li class="contact__item"><span class="contact__icon">w</span>www.brightorbitads-example.com</li>
    </ul>
    <div class="front__pixels" role="img" aria-label="Pixelated green square pattern trailing off the frame line"></div>
    <div class="brand">
      <span class="brand__mark"></span>
      <span class="brand__name">Bright<br>Orbit Ads</span>
    </div>
  </section>

  <section class="card card--back">
    <p class="back__url">
      <span class="back__url-prefix">www•</span><span class="back__url-domain">brightorbitads-example</span><span class="back__url-suffix">•com</span>
    </p>
    <div class="back__pixels" role="img" aria-label="Faint pixelated square pattern wrapping in from the front side"></div>
  </section>
</body>
</html>
```